Signage for a store*

logo on the two sides of the sign
in the middle is the name of the store witch is KORVELO
at the bottom of the two logos, one side for location/address and the other side is contact details phone number is 718-392-6170 address is 7342 THE SIGN WILL BEE 15 FEET BY 4 FEET I WOULD LIKE THAT THE
BACKGROUND OF THE SIGN SHOULD HAVE A NICE COLOR BASE
THAT GOES FOR A WINE STORE

```html
<!DOCTYPE html>
<html lang="en">
<head>
<meta charset="UTF-8">
<title>Korvelo Wine Store – Storefront Sign</title>
<link rel="stylesheet" href="https://fonts.googleapis.com/css2?family=Bodoni+Moda:wght@500;700&family=Playfair+Display:wght@700&display=swap">
<style>
  :root {
    --page: #ffffff;
    --sign: #000000;
    --gold-light: #f8dc6a;
    --gold-mid: #b98c3e;
    --gold-deep: #d9b23f;
    --gold-solid: #e2bd4f;
  }
  * { margin: 0; padding: 0; box-sizing: border-box; }
  html, body {
    width: 1200px;
    height: 432px;
    overflow: hidden;
    background: var(--page);
  }
  .canvas {
    position: relative;
    width: 1200px;
    height: 432px;
    background: var(--page);
  }
  .sign {
    position: absolute;
    left: 70px;
    top: 75px;
    width: 1059px;
    height: 283px;
    background: var(--sign);
  }
  .gold-text {
    background: linear-gradient(180deg, var(--gold-deep) 0%, var(--gold-light) 28%, var(--gold-mid) 55%, var(--gold-light) 78%, var(--gold-deep) 100%);
    -webkit-background-clip: text;
    background-clip: text;
    color: transparent;
  }
  .brand-mark {
    position: absolute;
    top: 36px;
    width: 180px;
    display: flex;
    flex-direction: column;
    align-items: center;
    gap: 10px;
  }
  .brand-mark--left { left: 45px; }
  .brand-mark--right { left: 835px; }
  .brand-mark__dot {
    width: 52px;
    height: 52px;
    border: 2px solid var(--gold-solid);
    border-radius: 50%;
  }
  .brand-mark__name {
    font-family: "Bodoni Moda", serif;
    font-weight: 500;
    font-size: 26px;
    letter-spacing: 1px;
    color: var(--gold-solid);
  }
  .store-name {
    position: absolute;
    left: 0;
    right: 0;
    top: 78px;
    text-align: center;
    font-family: "Bodoni Moda", serif;
    font-weight: 500;
    font-size: 116px;
    line-height: 1;
    letter-spacing: 3px;
  }
  .store-type {
    position: absolute;
    left: 0;
    right: 0;
    top: 210px;
    text-align: center;
    font-family: "Playfair Display", serif;
    font-weight: 700;
    font-size: 30px;
    line-height: 1;
    letter-spacing: 12px;
    padding-left: 12px;
  }
  .sign-detail {
    position: absolute;
    top: 230px;
    width: 220px;
    text-align: center;
    font-family: "Playfair Display", serif;
    font-weight: 700;
    font-size: 27px;
    line-height: 1;
  }
  .sign-detail--phone { left: 25px; }
  .sign-detail--address { left: 815px; }
</style>
</head>
<body>
  <main class="canvas">
    <section class="sign" aria-label="Korvelo Wine Store sign">
      <div class="brand-mark brand-mark--left">
        <span class="brand-mark__dot"></span>
        <span class="brand-mark__name">KORVELO</span>
      </div>

      <h1 class="store-name"><span class="gold-text">KORVELO</span></h1>
      <p class="store-type"><span class="gold-text">WINE STORE</span></p>

      <div class="brand-mark brand-mark--right">
        <span class="brand-mark__dot"></span>
        <span class="brand-mark__name">KORVELO</span>
      </div>

      <p class="sign-detail sign-detail--phone"><span class="gold-text">718-392-6170</span></p>
      <p class="sign-detail sign-detail--address"><span class="gold-text">7342</span></p>
    </section>
  </main>
</body>
</html>
```